Birch Landing

HI We need book cover design done for a physical book. See the attached document that represents the text that we want.

The book is about retiring with financial freedom.

```html
<!DOCTYPE html>
<html lang="en">
<head>
<meta charset="UTF-8">
<title>Confidence to Enjoy – Book Cover</title>
<link rel="stylesheet" href="https://fonts.googleapis.com/css2?family=Montserrat:wght@500;600;700;800&display=swap">
<style>
  :root {
    --sky-light: #5fb4d6;
    --sky: #4a9fc6;
    --sky-deep: #3f8fb6;
    --ink: #2b2f33;
    --orange: #f2602a;
    --switch-dark: #3a3d40;
    --switch-red: #d9343c;
  }
  * { margin: 0; padding: 0; box-sizing: border-box; }
  html, body { width: 800px; height: 1200px; overflow: hidden; }
  body { font-family: "Montserrat", Arial, sans-serif; }

  .cover {
    position: relative;
    width: 800px;
    height: 1200px;
    background: radial-gradient(ellipse at 50% 40%, var(--sky-light) 0%, var(--sky) 55%, var(--sky-deep) 100%);
    color: var(--ink);
    text-align: center;
    overflow: hidden;
  }

  .title { position: absolute; top: 120px; left: 0; width: 100%; }
  .title-top, .title-link, .title-main { display: block; line-height: 1; }
  .title-top {
    font-weight: 700;
    font-size: 76px;
    letter-spacing: 3px;
    color: var(--ink);
  }
  .title-link {
    margin-top: 18px;
    font-weight: 700;
    font-size: 40px;
    letter-spacing: 2px;
    color: var(--orange);
  }
  .title-main {
    margin-top: 6px;
    font-weight: 800;
    font-size: 150px;
    letter-spacing: 4px;
    color: var(--orange);
  }

  .subtitle {
    position: absolute;
    top: 432px;
    left: 0;
    width: 100%;
    font-size: 26px;
    line-height: 38px;
    letter-spacing: 0.5px;
    font-weight: 500;
    color: var(--ink);
  }
  .subtitle strong { font-weight: 700; }

  .switch-illustration {
    position: absolute;
    top: 606px;
    left: 265px;
    width: 270px;
    height: 438px;
    border-radius: 34px;
    background: linear-gradient(180deg, var(--switch-dark) 0%, var(--switch-red) 12%, #c42d35 55%, #a8232b 100%);
    box-shadow: 0 14px 28px rgba(0, 0, 0, 0.25);
  }

  .author {
    position: absolute;
    top: 1056px;
    left: 0;
    width: 100%;
    font-size: 56px;
    font-weight: 600;
    line-height: 1;
    color: var(--ink);
  }
  .author-role {
    position: absolute;
    top: 1134px;
    left: 0;
    width: 100%;
    font-size: 20px;
    font-weight: 600;
    color: var(--ink);
  }
</style>
</head>
<body>
  <main class="cover">
    <h1 class="title">
      <span class="title-top">CONFIDENCE</span>
      <span class="title-link">TO</span>
      <span class="title-main">ENJOY</span>
    </h1>

    <p class="subtitle">
      WHAT TO EXPECT<br>
      <strong>WHEN THE WORKDAYS END</strong><br>
      AND YOUR FREEDOM STARTS
    </p>

    <div class="switch-illustration" role="img" aria-label="Illustration of a red light switch in a dark frame, the upper half marked with an on line and the lower half with a dollar sign"></div>

    <p class="author">Daniel Hartwell</p>
    <p class="author-role">Host of The Steady Dollar Podcast And Freedom Years</p>
  </main>
</body>
</html>
```